20 year old business card needs re-design

We need to redesign our corporate business card look. We need something that appears more modern, eye catchy but professional.

Target Market(s)

manufacturing industry

Industry/Entity Type

Manufacturer

Contact Information for Business Card

One side can have the logo. Other side can have contact information.

Font styles to use
Serif

Colors
3277b5
33b8a4
ffffff

Requirements
Must have
• Eye catchy - need to standout from the crowd. company logo cannot change. Full name, job title, phone number and email address.
Should not have
• Fax, business address is not necessary.

```html
<!DOCTYPE html>
<html lang="en">
<head>
<meta charset="utf-8">
<title>Veltron Industrial – Business Card</title>
<link href="https://fonts.googleapis.com/css2?family=Arimo:wght@400;700&display=swap" rel="stylesheet">
<style>
  :root {
    --page-bg: #2b2b2d;
    --card-white: #ffffff;
    --card-shade: #eceef0;
    --brand-blue: #1d4fa6;
    --brand-ink: #151515;
    --band-text: #dfe6f2;
    --divider: #8fa6cf;
  }
  * { margin: 0; padding: 0; box-sizing: border-box; }
  html, body {
    width: 1200px;
    height: 997px;
    overflow: hidden;
    background: var(--page-bg);
    font-family: "Arimo", Arial, sans-serif;
  }
  .sheet {
    width: 1200px;
    height: 997px;
    display: flex;
    flex-direction: column;
    align-items: center;
    justify-content: center;
    gap: 48px;
  }
  .card {
    position: relative;
    width: 640px;
    height: 366px;
    background: linear-gradient(180deg, var(--card-white) 0%, var(--card-shade) 100%);
    overflow: hidden;
    box-shadow: 0 14px 30px rgba(0,0,0,.45);
  }
  .card-art {
    position: absolute;
    inset: 0;
    width: 100%;
    height: 100%;
  }
  .band { fill: var(--brand-blue); }
  .swoosh { fill: var(--brand-ink); }

  .wordmark {
    position: absolute;
    left: 0;
    right: 0;
    top: 62px;
    text-align: center;
    color: var(--brand-ink);
    font-weight: 700;
    line-height: 1;
  }
  .wordmark-name {
    display: block;
    font-size: 74px;
    letter-spacing: -2px;
  }
  .wordmark-sub {
    display: block;
    font-size: 17px;
    letter-spacing: 12px;
    margin-top: 4px;
    padding-left: 12px;
  }
  .card--front .wordmark { top: 82px; }

  .website {
    position: absolute;
    right: 40px;
    bottom: 46px;
    color: var(--card-white);
    font-weight: 700;
    font-size: 17px;
    letter-spacing: 1.5px;
  }

  .holder {
    position: absolute;
    left: 72px;
    bottom: 34px;
    color: var(--band-text);
    text-align: center;
  }
  .holder-name { font-size: 22px; font-weight: 700; letter-spacing: .5px; }
  .holder-title { font-size: 15px; font-weight: 700; margin-top: 3px; }

  .divider {
    position: absolute;
    left: 318px;
    top: 230px;
    width: 1px;
    height: 108px;
    background: var(--divider);
  }
  .contact-list {
    position: absolute;
    left: 340px;
    top: 228px;
    list-style: none;
    color: var(--band-text);
    font-size: 15px;
    line-height: 1.3;
  }
  .contact-item {
    display: flex;
    align-items: flex-start;
    gap: 8px;
    margin-bottom: 4px;
  }
  .contact-icon {
    flex: none;
    width: 16px;
    height: 16px;
    margin-top: 2px;
  }
  .contact-icon circle { fill: none; stroke: var(--band-text); stroke-width: 1.4; }
  .contact-icon .glyph { fill: var(--band-text); }
</style>
</head>
<body>
<main class="sheet">

  <section class="card card--front" aria-label="Card front">
    <svg class="card-art" viewBox="0 0 640 366" aria-hidden="true">
      <path class="band" d="M0 366 C 160 300 380 220 640 150 L640 366 Z"/>
      <path class="swoosh" d="M40 352 C 200 250 420 170 636 132 C 420 180 210 262 48 356 Z"/>
    </svg>
    <div class="wordmark">
      <span class="wordmark-name">Veltron</span>
      <span class="wordmark-sub">INDUSTRIAL</span>
    </div>
    <p class="website">WWW.VELTRONINDUSTRIAL.COM</p>
  </section>

  <section class="card card--back" aria-label="Card back">
    <svg class="card-art" viewBox="0 0 640 366" aria-hidden="true">
      <path class="band" d="M0 300 C 150 220 380 182 640 186 L640 366 L0 366 Z"/>
      <path class="swoosh" d="M24 276 C 170 196 400 160 610 166 C 400 164 175 202 30 280 Z"/>
    </svg>
    <div class="wordmark">
      <span class="wordmark-name">Veltron</span>
      <span class="wordmark-sub">INDUSTRIAL</span>
    </div>

    <div class="holder">
      <p class="holder-name">DANA MERCER</p>
      <p class="holder-title">Owner</p>
    </div>

    <span class="divider"></span>

    <ul class="contact-list">
      <li class="contact-item">
        <svg class="contact-icon" viewBox="0 0 16 16" aria-hidden="true">
          <circle cx="8" cy="8" r="7"/>
          <path class="glyph" d="M4.5 6.5h7v1.2l-1.2.8H5.7l-1.2-.8z M6 9h4v2.5H6z"/>
        </svg>
        <span>555-014-2780</span>
      </li>
      <li class="contact-item">
        <svg class="contact-icon" viewBox="0 0 16 16" aria-hidden="true">
          <circle cx="8" cy="8" r="7"/>
          <path class="glyph" d="M4.5 5.5h7v5h-7z M5 6l3 2.3L11 6v.8L8 9.1 5 6.8z" fill-rule="evenodd"/>
        </svg>
        <span>info@veltronindustrial.com</span>
      </li>
      <li class="contact-item">
        <svg class="contact-icon" viewBox="0 0 16 16" aria-hidden="true">
          <circle cx="8" cy="8" r="7"/>
          <path class="glyph" d="M8 3.8a2.6 2.6 0 0 1 2.6 2.6C10.6 8.4 8 12 8 12S5.4 8.4 5.4 6.4A2.6 2.6 0 0 1 8 3.8z"/>
        </svg>
        <span>P.O. Box 40217 Lakeview,<br>MI 48000</span>
      </li>
    </ul>
  </section>

</main>
</body>
</html>
```